new KVR one page flyer

We need a 1 page A4 size flyer (need it asap please) that describes on 1 page with art work and using photos the services we provide. I have included some examples of old previous flyers from our other (seperate divisions of the business) I have named a photo called (photo for top of design) however you do your design this photo needs to be the star of the page by either having it at the top or bottom of the page please and we usually like this photo to be in greyscale colour.
we do like greyscale designs but are open to see what you come up with as a whole page of grey white and black might not suit.

Needs to list the following

Services include:
Over size loads / Hot Shot Loads
Heavy Vehicle Recovery services
Potable Water Deliveries
Road Building / Maintenance
Earthworks
Sand & Metal Supply & Cartage
Road Train Tippers
Road Train Tankers
Road Train Flat Tops
Drop Deck Trailers
Mine site accredited equipment & Operators.

We offer a large rage of services not listed so call us today for a personalised quote to suit your needs.

To go on the bottom of the page our contact details are

KVR Pty Ltd
Depot: Lot 514, Banksia Flats Track Coober Pedy
Mobile: 047 216 9381
email: darren@kestrelvaleroadworks.com.au

Target Market(s)

new clients

Colors

Designer to choose colors to be used in the design.

Requirements
Must have
• our services listed
Nice to have
• stand out designs

```html
<!DOCTYPE html>
<html lang="en">
<head>
<meta charset="utf-8">
<title>KVR Services Flyer</title>
<link href="https://fonts.googleapis.com/css2?family=Orbitron:wght@700;900&family=Poppins:ital,wght@1,600;1,700;1,800&display=swap" rel="stylesheet">
<style>
  :root {
    --page-bg: #e4e4e4;
    --gold: #a87f40;
    --gold-light: #c2954f;
    --charcoal: #2b2724;
    --slate-dark: #353535;
    --slate-mid: #4b4b4b;
    --silver: #cfcfcf;
    --cream: #efe3cc;
    --white: #ffffff;
    --ink: #1f1f1f;
  }
  * { box-sizing: border-box; margin: 0; padding: 0; }
  html, body {
    width: 1200px; height: 1200px; overflow: hidden;
    background: var(--page-bg);
  }
  .flyer {
    position: absolute; left: 210px; top: 48px;
    width: 780px; height: 1103px; overflow: hidden;
    background: var(--slate-dark);
    box-shadow: 0 6px 18px rgba(0,0,0,.35);
    font-family: "Poppins", sans-serif; font-style: italic;
  }
  .abs { position: absolute; }

  /* header */
  .header {
    left: 0; top: 0; width: 780px; height: 148px;
    background: linear-gradient(100deg, #7a7a7a 0%, #5a5a5a 40%, #3d3d3d 100%);
  }
  .top-strip { left: 0; top: 0; width: 780px; height: 9px; background: var(--gold); }
  .brand-mark {
    left: 34px; top: 28px;
    font-family: "Poppins", sans-serif; font-style: italic; font-weight: 800;
    font-size: 96px; line-height: 1; letter-spacing: 4px;
    color: var(--silver);
  }
  .name-panel { left: 380px; top: 37px; width: 400px; height: 111px; }
  .company-name {
    right: 30px; top: 56px; text-align: right;
    font-family: "Orbitron", sans-serif; font-style: normal; font-weight: 900;
    font-size: 30px; line-height: 36px; letter-spacing: 1px;
    color: var(--cream);
  }

  /* web band */
  .web-band {
    left: 0; top: 148px; width: 780px; height: 32px;
    background: var(--gold);
  }
  .web-address {
    right: 24px; top: 3px;
    font-weight: 700; font-size: 20px; color: var(--white);
  }

  /* hero photo */
  .hero-photo {
    left: 0; top: 180px; width: 780px; height: 269px;
    background: linear-gradient(180deg, #d4d4d4 0%, #9c9c9c 35%, #3a3a3a 55%, #8a8a8a 75%, #b5b5b5 100%);
  }
  .services-banner { left: 370px; top: 405px; width: 410px; height: 44px; }
  .services-title {
    right: 24px; top: 410px;
    font-family: "Orbitron", sans-serif; font-style: normal; font-weight: 700;
    font-size: 27px; letter-spacing: 1px; color: var(--white);
  }

  /* services area */
  .services-area {
    left: 0; top: 449px; width: 780px; height: 591px;
    background: linear-gradient(160deg, #3a3836 0%, #2d2b29 50%, #3e3c3a 100%);
  }
  .truck-photo { left: 0; top: 449px; width: 440px; height: 591px; }

  .service-list { list-style: none; }
  .service {
    position: absolute; white-space: nowrap;
    font-weight: 700; font-size: 21px; line-height: 28px; color: var(--white);
  }
  .service::before {
    content: ""; display: inline-block; width: 6px; height: 6px;
    border-radius: 50%; background: var(--gold-light);
    margin-right: 8px; vertical-align: middle; position: relative; top: -3px;
  }
  .service.continued::before { display: none; }

  .quote-note {
    left: 470px; top: 900px; width: 300px; text-align: center;
    font-weight: 700; font-size: 16.5px; line-height: 21px; color: var(--gold-light);
  }

  .phone-pill {
    left: 444px; top: 1000px; width: 336px; height: 41px;
    background: var(--white); border-radius: 21px 0 0 21px;
  }
  .phone-icon { left: 470px; top: 1006px; }
  .phone-number {
    left: 512px; top: 1000px;
    font-weight: 800; font-size: 28px; line-height: 41px; color: var(--ink);
  }

  /* footer */
  .footer {
    left: 0; top: 1040px; width: 780px; height: 63px;
    background: var(--slate-mid);
  }
  .contact-line {
    position: absolute; left: 49px;
    font-weight: 700; font-size: 13.5px; line-height: 18px; color: var(--white);
  }
  .contact-icon { position: absolute; left: 24px; }
</style>
</head>
<body>
  <main class="flyer">
    <header>
      <div class="abs header"></div>
      <div class="abs top-strip"></div>
      <div class="abs brand-mark">KVR</div>
      <svg class="abs name-panel" viewBox="0 0 400 111" aria-hidden="true">
        <polygon points="90,0 400,0 400,111 0,111" fill="var(--charcoal)"/>
      </svg>
      <div class="abs company-name">KESTREL VALE<br>ROADWORKS</div>
    </header>

    <div class="abs web-band"></div>
    <div class="abs web-address">www.kestrelvaleroadworks.com.au</div>

    <div class="abs hero-photo" role="img" aria-label="Greyscale photo of a road train tipper with three trailers on an outback dirt road"></div>
    <svg class="abs services-banner" viewBox="0 0 410 44" aria-hidden="true">
      <polygon points="40,0 410,0 410,44 0,44" fill="var(--gold)"/>
    </svg>
    <h2 class="abs services-title">OUR SERVICES</h2>

    <section>
      <div class="abs services-area"></div>
      <svg class="abs truck-photo" viewBox="0 0 440 591" role="img" aria-label="Colour photo of a white prime mover truck on red outback earth under a blue sky">
        <defs>
          <linearGradient id="truckTones" x1="0" y1="0" x2="0" y2="1">
            <stop offset="0" stop-color="#3f78c4"/>
            <stop offset="0.3" stop-color="#8fb4de"/>
            <stop offset="0.55" stop-color="#c8c8c6"/>
            <stop offset="0.8" stop-color="#9a5a34"/>
            <stop offset="1" stop-color="#7a4426"/>
          </linearGradient>
        </defs>
        <polygon points="0,0 132,0 420,591 0,591" fill="url(#truckTones)"/>
      </svg>

      <ul class="service-list">
        <li class="service" style="left:272px;top:488px">Over size loads / Hot Shot Loads</li>
        <li class="service" style="left:289px;top:519px">Heavy Vehicle Recovery services</li>
        <li class="service" style="left:308px;top:550px">Portable Water Deliveries</li>
        <li class="service" style="left:326px;top:582px">Road Building / Maintenance</li>
        <li class="service" style="left:339px;top:613px">Earthworks</li>
        <li class="service" style="left:356px;top:645px">Sand &amp; Metal Supply &amp; Cartage</li>
        <li class="service" style="left:375px;top:676px">Road Train Tippers</li>
        <li class="service" style="left:387px;top:708px">Road Train Tankers</li>
        <li class="service" style="left:405px;top:739px">Road Train Flat Tops</li>
        <li class="service" style="left:422px;top:771px">Drop Deck Trailers</li>
        <li class="service" style="left:435px;top:802px">Mine site accredited</li>
        <li class="service continued" style="left:460px;top:834px">equipment &amp; Operators</li>
      </ul>

      <p class="abs quote-note">We offer a large rage of services not listed so call us today for a personalised quote to suit your needs.</p>

      <div class="abs phone-pill"></div>
      <svg class="abs phone-icon" width="30" height="30" viewBox="0 0 30 30" aria-hidden="true">
        <circle cx="15" cy="15" r="14" fill="var(--gold)"/>
        <path d="M10.5 8.5c.8-.6 1.8-.4 2.3.4l1.3 2.1c.4.7.2 1.5-.4 2l-1 .8c.8 1.8 2.2 3.3 4 4.2l.8-1c.5-.6 1.4-.8 2-.3l2 1.4c.8.5 1 1.6.3 2.3l-1 1.1c-.9.9-2.3 1.1-3.5.6-3.8-1.7-6.8-4.7-8.4-8.5-.5-1.2-.2-2.6.7-3.4z" fill="var(--white)"/>
      </svg>
      <div class="abs phone-number">047 216 9381</div>
    </section>

    <footer>
      <div class="abs footer">
        <div class="contact-line" style="top:4px">KVR Pty Ltd</div>
        <svg class="contact-icon" style="top:22px" width="12" height="16" viewBox="0 0 12 16" aria-hidden="true">
          <path d="M6 0C2.7 0 0 2.6 0 5.9 0 10.3 6 16 6 16s6-5.7 6-10.1C12 2.6 9.3 0 6 0zm0 8.3a2.4 2.4 0 1 1 0-4.8 2.4 2.4 0 0 1 0 4.8z" fill="var(--gold-light)"/>
        </svg>
        <div class="contact-line" style="top:22px">Depot: Lot 514, Banksia Flats Track Coober Pedy</div>
        <svg class="contact-icon" style="top:45px" width="13" height="9" viewBox="0 0 13 9" aria-hidden="true">
          <rect x="0.6" y="0.6" width="11.8" height="7.8" fill="none" stroke="var(--gold-light)" stroke-width="1.2"/>
          <path d="M0.6 0.6 6.5 5 12.4 0.6" fill="none" stroke="var(--gold-light)" stroke-width="1.2"/>
        </svg>
        <div class="contact-line" style="top:40px">darren@kestrelvaleroadworks.com.au</div>
      </div>
    </footer>
  </main>
</body>
</html>
```